Corvane 718Q

We are a consulting firm we a bad website and would like it to look more professional. We are a consulting firm that help people with the 340b drug program. We help non profit clinics get more funding.

Please reference our current website https://www.corvane718q.com/ for ideas

We also want a seperate webpage for each of "our services" see attachments.

Industry/Entity Type

consulting, medical, compliance

Coding

Coded - Design and coding required

Number of Pages Required

5+ page

Requirements
Must have
• Professional, my logo from my original website. It should look good
Nice to have
• It needs to be professional

```html
<!DOCTYPE html>
<html lang="en">
<head>
<meta charset="utf-8">
<title>Corvane 718Q — Turnkey 340B Program Development &amp; Management</title>
<link href="https://fonts.googleapis.com/css2?family=Plus+Jakarta+Sans:wght@400;500;600;700;800&display=swap" rel="stylesheet">
<style>
:root{
  --teal-900:#0a3334;
  --teal-800:#0d4344;
  --teal-700:#125556;
  --green:#2e9e74;
  --green-light:#e3f3ec;
  --mint:#f2f7f5;
  --ink:#12292a;
  --muted:#5b6b6c;
  --line:#dde6e3;
  --white:#ffffff;
}
*{box-sizing:border-box;margin:0;padding:0}
html,body{width:816px;height:1200px;overflow:hidden}
body{font-family:"Plus Jakarta Sans",Arial,sans-serif;color:var(--ink);background:var(--white);font-size:7px;line-height:1.45}
.wrap{padding:0 34px}
.btn{display:inline-flex;align-items:center;gap:4px;font-weight:600;font-size:7px;padding:7px 11px;border-radius:4px;white-space:nowrap}
.btn-green{background:var(--green);color:var(--white)}
.btn-ghost{border:1px solid rgba(255,255,255,.55);color:var(--white)}
.btn-outline{border:1px solid var(--teal-800);color:var(--teal-800)}
.eyebrow{font-size:6px;font-weight:700;letter-spacing:.12em;text-transform:uppercase;color:var(--green)}

/* header */
.site-header{height:44px;display:flex;align-items:center;justify-content:space-between;border-bottom:1px solid var(--line)}
.brand{display:flex;align-items:center;gap:6px;font-weight:700;font-size:13px;color:var(--teal-800)}
.brand-dot{width:14px;height:14px;border-radius:50%;background:var(--green)}
.nav{display:flex;gap:20px;font-size:7px;font-weight:500;color:var(--ink)}
.nav .active{color:var(--green);border-bottom:1.5px solid var(--green);padding-bottom:3px}

/* hero */
.hero{height:270px;background:var(--teal-800);display:flex;color:var(--white)}
.hero-copy{width:400px;padding:18px 0 0 34px}
.crumbs{font-size:6px;color:rgba(255,255,255,.7);margin-bottom:20px}
.hero .eyebrow{color:#7fd3b0;margin-bottom:8px}
.hero h1{font-size:24px;line-height:1.18;font-weight:800;margin-bottom:12px}
.hero p{font-size:7.5px;color:rgba(255,255,255,.82);max-width:330px;margin-bottom:18px}
.hero-actions{display:flex;gap:8px}
.hero-photo{flex:1;background:linear-gradient(135deg,#b9cfcc 0%,#7f9f9b 55%,#4d6e6c 100%);border-bottom-left-radius:60px}

/* value + overview */
.pillars{height:300px;display:flex;gap:26px;padding:24px 34px 0;background:var(--mint)}
.value-card{width:300px;background:var(--white);border-radius:6px;padding:18px;border:1px solid var(--line);height:250px}
.value-card h2,.overview h2{font-size:15px;line-height:1.22;font-weight:800;color:var(--teal-800);margin:6px 0 8px}
.value-card p{color:var(--muted);margin-bottom:12px}
.checks{list-style:none;display:grid;gap:9px}
.checks li{display:flex;align-items:center;gap:7px;font-weight:500}
.tick{width:12px;height:12px;flex:none}
.overview{flex:1}
.overview>p{color:var(--muted);margin-bottom:12px;max-width:380px}
.services{display:grid;gap:10px}
.service{display:flex;gap:10px;align-items:flex-start}
.service-icon{width:24px;height:24px;border-radius:5px;background:var(--green-light);display:flex;align-items:center;justify-content:center;flex:none}
.service h3{font-size:8px;font-weight:700;color:var(--teal-800)}
.service p{color:var(--muted)}

/* process */
.process{height:175px;text-align:center;padding-top:20px}
.process h2{font-size:15px;font-weight:800;color:var(--teal-800);margin:4px 0 16px}
.steps{display:flex;justify-content:space-between;padding:0 60px;position:relative}
.steps::before{content:"";position:absolute;left:110px;right:110px;top:17px;border-top:1px dashed #9fcab7}
.step{width:110px;position:relative}
.step-num{width:34px;height:34px;border-radius:50%;background:var(--teal-800);color:var(--white);display:flex;align-items:center;justify-content:center;font-weight:700;font-size:10px;margin:0 auto 7px;border:3px solid var(--green-light)}
.step h3{font-size:8px;font-weight:700;color:var(--teal-800);margin-bottom:3px}
.step p{color:var(--muted);font-size:6.5px}

/* results */
.results{height:205px;background:var(--mint);padding:18px 34px 0}
.results-head{display:flex;justify-content:space-between;align-items:flex-end;margin-bottom:12px}
.results h2{font-size:15px;font-weight:800;color:var(--teal-800);margin-top:4px}
.cases{display:grid;grid-template-columns:repeat(3,1fr);gap:14px}
.case{background:var(--white);border:1px solid var(--line);border-radius:6px;padding:12px}
.case-top{display:flex;gap:7px;align-items:center;margin-bottom:10px}
.case-icon{width:20px;height:20px;border-radius:4px;background:var(--green-light)}
.case h3{font-size:8px;font-weight:700;color:var(--teal-800)}
.case-top span{color:var(--muted);font-size:6px}
.stats{display:grid;grid-template-columns:repeat(3,1fr);gap:6px;margin-bottom:10px}
.stat b{display:block;font-size:12px;font-weight:800;color:var(--teal-800)}
.stat span{font-size:6px;color:var(--muted)}
.case a{font-size:6.5px;font-weight:600;color:var(--green);text-decoration:none}

/* cta */
.cta-outer{height:72px;padding:6px 34px 0}
.cta{height:58px;background:var(--teal-900);border-radius:6px;display:flex;align-items:center;justify-content:space-between;padding:0 22px;color:var(--white)}
.cta-left{display:flex;align-items:center;gap:12px}
.cta-icon{width:28px;height:28px;border-radius:50%;background:var(--green)}
.cta h2{font-size:12px;font-weight:700}
.cta p{color:rgba(255,255,255,.75)}
.cta-actions{display:flex;gap:8px}

/* footer */
.site-footer{height:134px;background:var(--teal-900);color:rgba(255,255,255,.75);padding:18px 34px 0}
.foot-grid{display:grid;grid-template-columns:1.6fr 1fr 1.3fr 1fr 1.2fr;gap:18px}
.site-footer .brand{color:var(--white);font-size:12px;margin-bottom:6px}
.foot-grid h4{color:var(--white);font-size:7px;font-weight:700;margin-bottom:5px}
.foot-grid ul{list-style:none;display:grid;gap:2px;font-size:6.5px}
.socials{display:flex;gap:5px;margin-top:7px}
.socials span{width:12px;height:12px;border-radius:50%;background:rgba(255,255,255,.2)}
.foot-bottom{border-top:1px solid rgba(255,255,255,.15);margin-top:12px;padding-top:7px;display:flex;justify-content:space-between;font-size:6px}
</style>
</head>
<body>

<header class="site-header wrap">
  <div class="brand"><span class="brand-dot"></span>Corvane 718Q</div>
  <nav class="nav">
    <span>Home</span><span>About Us</span><span class="active">Our Services</span><span>Why Corvane 718Q</span><span>Resources</span><span>Contact Us</span>
  </nav>
  <span class="btn btn-green">Schedule a Consultation →</span>
</header>

<section class="hero">
  <div class="hero-copy">
    <div class="crumbs">Home › Our Services › Turnkey 340B Program Development &amp; Management</div>
    <div class="eyebrow">340B Solutions</div>
    <h1>Turnkey 340B Program Development &amp; Management</h1>
    <p>We build, launch, and manage 340B programs that drive measurable financial impact and expand access to care. From initial design and HRSA registration to ongoing oversight, we're with you every step of the way.</p>
    <div class="hero-actions">
      <span class="btn btn-green">Schedule a Consultation →</span>
      <span class="btn btn-ghost">Explore All Services</span>
    </div>
  </div>
  <div class="hero-photo" role="img" aria-label="Photo of three smiling healthcare consultants in business attire"></div>
</section>

<section class="pillars">
  <div class="value-card">
    <div class="eyebrow">The Value</div>
    <h2>Build a Strong Foundation.<br>Drive Lasting Impact.</h2>
    <p>A well-designed and well-managed 340B program can generate millions in savings, reduce drug costs for vulnerable patients, and strengthen your organization's financial health.</p>
    <ul class="checks">
      <li><svg class="tick" viewBox="0 0 12 12"><circle cx="6" cy="6" r="6" fill="#2e9e74"/><path d="M3.4 6.2l1.8 1.8 3.4-3.6" stroke="#fff" stroke-width="1.3" fill="none"/></svg>Maximize savings and reinvest in care</li>
      <li><svg class="tick" viewBox="0 0 12 12"><circle cx="6" cy="6" r="6" fill="#2e9e74"/><path d="M3.4 6.2l1.8 1.8 3.4-3.6" stroke="#fff" stroke-width="1.3" fill="none"/></svg>Ensure compliance and reduce risk</li>
      <li><svg class="tick" viewBox="0 0 12 12"><circle cx="6" cy="6" r="6" fill="#2e9e74"/><path d="M3.4 6.2l1.8 1.8 3.4-3.6" stroke="#fff" stroke-width="1.3" fill="none"/></svg>Streamline operations and save time</li>
      <li><svg class="tick" viewBox="0 0 12 12"><circle cx="6" cy="6" r="6" fill="#2e9e74"/><path d="M3.4 6.2l1.8 1.8 3.4-3.6" stroke="#fff" stroke-width="1.3" fill="none"/></svg>Expand access to essential medications</li>
    </ul>
  </div>
  <div class="overview">
    <div class="eyebrow">Service Overview</div>
    <h2>End-to-End Support for 340B Success</h2>
    <p>Our turnkey approach covers every aspect of your 340B program, from strategy and setup to day-to-day management and optimization.</p>
    <div class="services">
      <div class="service"><div class="service-icon"><svg width="12" height="12" viewBox="0 0 12 12"><rect x="2" y="1.5" width="8" height="9" rx="1" stroke="#125556" fill="none"/><path d="M4 4.5h4M4 6.5h4M4 8.5h2.5" stroke="#125556"/></svg></div><div><h3>Program Design &amp; Implementation</h3><p>We assess your organization's needs and design a customized 340B program built for long-term success.</p></div></div>
      <div class="service"><div class="service-icon"><svg width="12" height="12" viewBox="0 0 12 12"><path d="M6 1.5l4 1.6v3c0 2.4-1.8 3.8-4 4.4-2.2-.6-4-2-4-4.4v-3z" stroke="#125556" fill="none"/></svg></div><div><h3>HRSA Registration &amp; Renewals</h3><p>We handle all HRSA registrations, recertifications, and required documentation to keep your program active and compliant.</p></div></div>
      <div class="service"><div class="service-icon"><svg width="12" height="12" viewBox="0 0 12 12"><circle cx="4" cy="4" r="2" stroke="#125556" fill="none"/><circle cx="8.5" cy="5" r="1.6" stroke="#125556" fill="none"/><path d="M1 10c.5-2 1.6-3 3-3s2.5 1 3 3M7 10c.3-1.4 1-2.2 1.5-2.2S10.7 8.6 11 10" stroke="#125556" fill="none"/></svg></div><div><h3>Vendor &amp; Contract Management</h3><p>We help you select the right partners and negotiate contracts that maximize your value.</p></div></div>
      <div class="service"><div class="service-icon"><svg width="12" height="12" viewBox="0 0 12 12"><path d="M1.5 9l3-3 2 2 4-4.5" stroke="#125556" fill="none"/><path d="M8 3.5h2.5V6" stroke="#125556" fill="none"/></svg></div><div><h3>Ongoing Program Oversight</h3><p>We provide continuous monitoring, reporting, and compliance support so you can focus on your mission.</p></div></div>
    </div>
  </div>
</section>

<section class="process">
  <div class="eyebrow">Our Process</div>
  <h2>A Proven Approach to Program Success</h2>
  <div class="steps">
    <div class="step"><div class="step-num">1</div><h3>Discover</h3><p>We learn about your organization, challenges, and goals.</p></div>
    <div class="step"><div class="step-num">2</div><h3>Assess</h3><p>We evaluate your current program and identify opportunities.</p></div>
    <div class="step"><div class="step-num">3</div><h3>Strategize</h3><p>We develop a customized plan aligned with your mission and objectives.</p></div>
    <div class="step"><div class="step-num">4</div><h3>Implement</h3><p>We put the plan into action with expert guidance and support.</p></div>
    <div class="step"><div class="step-num">5</div><h3>Optimize</h3><p>We continuously monitor, measure, and refine for lasting impact.</p></div>
  </div>
</section>

<section class="results">
  <div class="results-head">
    <div><div class="eyebrow">Impact in Action</div><h2>Real Results. Real Impact.</h2></div>
    <span class="btn btn-outline">View All Case Studies →</span>
  </div>
  <div class="cases">
    <article class="case">
      <div class="case-top"><div class="case-icon"></div><div><h3>Community Health Center</h3><span>Multi-site FQHC</span></div></div>
      <div class="stats">
        <div class="stat"><b>$2.1M+</b><span>Savings in Year 1</span></div>
        <div class="stat"><b>28%</b><span>Increase in Patient Access</span></div>
        <div class="stat"><b>100%</b><span>HRSA Compliance</span></div>
      </div>
      <a>View Case Study →</a>
    </article>
    <article class="case">
      <div class="case-top"><div class="case-icon"></div><div><h3>Regional Hospital</h3><span>DSH Hospital</span></div></div>
      <div class="stats">
        <div class="stat"><b>$4.5M+</b><span>Annual Savings</span></div>
        <div class="stat"><b>30%</b><span>Reduction in Drug Costs</span></div>
        <div class="stat"><b>0</b><span>Audit Findings</span></div>
      </div>
      <a>View Case Study →</a>
    </article>
    <article class="case">
      <div class="case-top"><div class="case-icon"></div><div><h3>Critical Access Hospital</h3><span>Rural Hospital</span></div></div>
      <div class="stats">
        <div class="stat"><b>$1.2M+</b><span>Savings in Year 1</span></div>
        <div class="stat"><b>45%</b><span>Increase in Program Revenue</span></div>
        <div class="stat"><b>100%</b><span>HRSA Compliance</span></div>
      </div>
      <a>View Case Study →</a>
    </article>
  </div>
</section>

<div class="cta-outer">
  <section class="cta">
    <div class="cta-left"><div class="cta-icon"></div><div><h2>Ready to Maximize Your 340B Program?</h2><p>Schedule a consultation to learn how we can help your organization thrive.</p></div></div>
    <div class="cta-actions"><span class="btn btn-green">Schedule a Consultation →</span><span class="btn btn-ghost">Explore All Services</span></div>
  </section>
</div>

<footer class="site-footer">
  <div class="foot-grid">
    <div>
      <div class="brand"><span class="brand-dot"></span>Corvane 718Q</div>
      <p>Helping nonprofit clinics and hospitals unlock the full value of the 340B program to expand access to care.</p>
      <div class="socials"><span></span><span></span><span></span></div>
    </div>
    <div><h4>Quick Links</h4><ul><li>Home</li><li>About Us</li><li>Our Services</li><li>Why Corvane 718Q</li><li>Contact Us</li></ul></div>
    <div><h4>Our Services</h4><ul><li>Turnkey 340B Program Development</li><li>HRSA Registration &amp; Renewals</li><li>Vendor &amp; Contract Management</li><li>Compliance &amp; Audit Support</li><li>Ongoing Program Oversight</li></ul></div>
    <div><h4>Resources</h4><ul><li>Blog</li><li>Case Studies</li><li>Guides</li><li>FAQs</li><li>Events</li></ul></div>
    <div><h4>Contact</h4><ul><li>(555) 014-2290</li><li>hello@corvane718q.com</li><li>www.corvane718q.com</li></ul></div>
  </div>
  <div class="foot-bottom"><span>© 2025 Corvane 718Q. All rights reserved.</span><span>Privacy Policy · Terms of Service</span></div>
</footer>

</body>
</html>
```